Re-Design for our current Business card

Would like a re-design to a horizontal business card, split in to two sides similar to your previous submission. We want them on a horizontal, take off the additional graphics on the corners make it more simple. We

```html
<!DOCTYPE html>
<html lang="en">
<head>
<meta charset="utf-8">
<title>Brightway Wellness Group – Business Card</title>
<link href="https://fonts.googleapis.com/css2?family=Montserrat:wght@400;500;600;700&display=swap" rel="stylesheet">
<style>
  :root {
    --stage: #2b2b2b;
    --card-dark: #050505;
    --card-light: #ffffff;
    --brand-blue: #1672bd;
    --brand-orange: #f2921f;
    --ink: #1c1c1c;
  }
  * { margin: 0; padding: 0; box-sizing: border-box; }
  html, body {
    width: 1200px; height: 875px; overflow: hidden;
    background: var(--stage);
    font-family: "Montserrat", sans-serif;
  }
  .sheet {
    width: 1200px; height: 875px;
    display: flex; align-items: center; justify-content: center; gap: 40px;
  }
  .card {
    width: 540px; height: 309px;
    border-radius: 18px;
    position: relative; overflow: hidden;
  }
  .card--front {
    background: var(--card-dark);
    display: flex; align-items: center; justify-content: center;
  }
  .card--back { background: var(--card-light); }

  .wordmark {
    display: flex; align-items: center; gap: 12px;
    color: var(--brand-blue); font-weight: 700;
    text-transform: uppercase; letter-spacing: -0.5px;
  }
  .wordmark__dot {
    border-radius: 50%; background: var(--brand-orange); flex: none;
  }
  .card--front .wordmark { font-size: 30px; line-height: 1.05; }
  .card--front .wordmark__dot { width: 46px; height: 46px; }

  .card--back .wordmark {
    position: absolute; left: 40px; top: 62px;
    font-size: 20px; line-height: 1.05;
  }
  .card--back .wordmark__dot { width: 30px; height: 30px; }

  .identity {
    position: absolute; left: 40px; top: 150px;
    width: 200px;
  }
  .identity__name {
    color: var(--brand-blue); font-weight: 700; font-size: 24px;
  }
  .identity__role {
    color: var(--ink); font-size: 12px; font-weight: 500; margin-top: 2px;
  }
  .divider {
    position: absolute; left: 242px; top: 142px;
    width: 1.5px; height: 64px; background: var(--brand-blue);
  }
  .contacts {
    position: absolute; left: 258px; top: 140px;
    list-style: none; font-size: 12.5px; color: var(--ink);
  }
  .contacts li { display: flex; align-items: center; gap: 8px; height: 22px; }
  .contacts svg { width: 12px; height: 12px; fill: var(--brand-orange); flex: none; }
  .address {
    position: absolute; left: 40px; top: 240px;
    font-size: 12.5px; color: var(--ink);
  }
</style>
</head>
<body>
<main class="sheet">
  <section class="card card--front" aria-label="Card front">
    <div class="wordmark">
      <span class="wordmark__dot"></span>
      <span>Brightway Wellness<br>Group</span>
    </div>
  </section>

  <section class="card card--back" aria-label="Card back">
    <div class="wordmark">
      <span class="wordmark__dot"></span>
      <span>Brightway Wellness<br>Group</span>
    </div>

    <div class="identity">
      <p class="identity__name">Daniel Hart</p>
      <p class="identity__role">Managing Director</p>
    </div>
    <div class="divider"></div>

    <ul class="contacts">
      <li>
        <svg viewBox="0 0 24 24"><path d="M6.6 10.8a15.1 15.1 0 0 0 6.6 6.6l2.2-2.2a1 1 0 0 1 1-.25 11.4 11.4 0 0 0 3.6.57 1 1 0 0 1 1 1V20a1 1 0 0 1-1 1A17 17 0 0 1 3 4a1 1 0 0 1 1-1h3.5a1 1 0 0 1 1 1c0 1.25.2 2.45.57 3.57a1 1 0 0 1-.25 1z"/></svg>
        (08) 5550 1234
      </li>
      <li>
        <svg viewBox="0 0 24 24"><path d="M2 5h20v14H2z M2 5l10 8 10-8" stroke="#fff" stroke-width="1.5"/></svg>
        info@brightwaywell.com
      </li>
      <li>
        <svg viewBox="0 0 24 24"><circle cx="12" cy="12" r="10"/></svg>
        www.brightwaywell.com
      </li>
    </ul>

    <p class="address">48 Harbor Lane, Fairview, USA</p>
  </section>
</main>
</body>
</html>
```